A Real Estate Company Needs a Business Card Design

We need a business card design for a new company based in Boston MA called "Brellmont Real Estate LLC" we are a small company but we like a big corporate look, a simple, sleek, modern and progressive look. we would like the option of having a design that could include the real estate agents personal photo and also a design if the realtor decides not to have a photo. we do not have LOGO at this moment, please use any property look pic corporate with word" Brellmont Real Estate LLC" please see attached file as an example.

```html
<!DOCTYPE html>
<html lang="en">
<head>
<meta charset="UTF-8">
<title>Brellmont Real Estate LLC – Business Card</title>
<link rel="stylesheet" href="https://fonts.googleapis.com/css2?family=Arimo:wght@400;700&display=swap">
<style>
  :root {
    --page-bg: #d9d9d9;
    --card-white: #f4f4f2;
    --brand-green: #00a03c;
    --brand-blue: #0a7cc8;
    --text-light: #ffffff;
    --shadow: rgba(0,0,0,0.18);
  }
  html, body {
    margin: 0;
    width: 1200px;
    height: 1000px;
    overflow: hidden;
    background: var(--page-bg);
    font-family: "Arimo", Arial, sans-serif;
  }
  .canvas {
    position: relative;
    width: 1200px;
    height: 1000px;
  }
  .card {
    position: absolute;
    width: 760px;
    height: 434px;
    background: var(--card-white);
    box-shadow: 0 6px 18px var(--shadow);
    overflow: hidden;
  }
  .card svg.card-shapes {
    position: absolute;
    inset: 0;
    width: 100%;
    height: 100%;
  }
  .card--front { left: 220px; top: 50px; }
  .card--back  { left: 220px; top: 516px; }

  .brand-name {
    position: absolute;
    color: var(--brand-green);
    font-weight: 700;
    text-transform: uppercase;
    letter-spacing: 0.04em;
    line-height: 1.15;
    margin: 0;
  }
  .brand-mark {
    display: block;
    background: var(--brand-blue);
  }
  .card--front .brand {
    position: absolute;
    left: 0; right: 0;
    top: 120px;
    display: flex;
    flex-direction: column;
    align-items: center;
    gap: 18px;
  }
  .card--front .brand-mark { width: 70px; height: 70px; }
  .card--front .brand-name {
    position: static;
    font-size: 34px;
    text-align: center;
  }
  .card--back .brand {
    position: absolute;
    left: 40px;
    top: 34px;
    display: flex;
    align-items: center;
    gap: 12px;
  }
  .card--back .brand-mark { width: 30px; height: 30px; }
  .card--back .brand-name {
    position: static;
    font-size: 18px;
  }

  .holder {
    position: absolute;
    left: 520px;
    top: 120px;
    color: var(--text-light);
  }
  .holder-name { font-size: 28px; font-weight: 700; margin: 0; }
  .holder-title { font-size: 17px; font-weight: 700; margin: 4px 0 0; }

  .contact {
    position: absolute;
    left: 180px;
    top: 262px;
    margin: 0;
    padding: 0;
    list-style: none;
    color: var(--text-light);
    font-size: 19px;
    line-height: 1.45;
  }
  .address {
    position: absolute;
    left: 160px;
    top: 382px;
    margin: 0;
    color: var(--text-light);
    font-size: 19px;
  }
</style>
</head>
<body>
<main class="canvas">

  <section class="card card--front" aria-label="Business card front">
    <svg class="card-shapes" viewBox="0 0 760 434" preserveAspectRatio="none" aria-hidden="true">
      <path d="M0,0 L230,0 Q80,18 0,110 Z" fill="var(--brand-green)"/>
      <path d="M760,220 Q745,410 420,434 L760,434 Z" fill="var(--brand-blue)"/>
    </svg>
    <div class="brand">
      <span class="brand-mark"></span>
      <p class="brand-name">Brellmont<br>Real Estate LLC</p>
    </div>
  </section>

  <section class="card card--back" aria-label="Business card back">
    <svg class="card-shapes" viewBox="0 0 760 434" preserveAspectRatio="none" aria-hidden="true">
      <path d="M0,330 Q300,90 760,30 L760,434 L0,434 Z" fill="var(--brand-blue)"/>
      <path d="M110,434 Q330,140 760,50 L760,434 Z" fill="var(--brand-green)"/>
    </svg>
    <div class="brand">
      <span class="brand-mark"></span>
      <p class="brand-name">Brellmont<br>Real Estate LLC</p>
    </div>
    <div class="holder">
      <p class="holder-name">Your Name</p>
      <p class="holder-title">Title</p>
    </div>
    <ul class="contact">
      <li>P : 012- 345- 6789</li>
      <li>E : yourname@mail.com</li>
      <li>W : www.address.com</li>
    </ul>
    <p class="address">A : Maple Row, 2190 Cedarvale, Boston, USA</p>
  </section>

</main>
</body>
</html>
```